Velvet Horizon Voyages Inc. We are looking for a skilled designer for our new Logo, Letterhead and Biz Car

We are looking for a fresh logo design for our new travel business. We excel in maximizing reward points for our clients that are high limit spenders or business owners, that can accumulate above average pools of airline, bank and travel points. Our core sales are in personal travel that crosses-over to business travel. Luxury Travel images and themes are essential in the design of the logo and biz cards. The letterhead can remain clean and refined.

Target Market(s)

Luxury Travelers and Business Owners that use reward point credit cards and programs to enhance their travel experiences.

Industry/Entity Type

Travel

Contact Information for Business Card

212 Pinecrest Hollow Rd NW
Calgary, Alberta T2K 4W9 Canada
Tel: (403)271-4408
kdelane@velvethorizonvoyages.com
www.velvethorizonvoyages.com

Logo Text

Velvet Horizon Voyages Inc.

Requirements
Must have
• Luxury Travel Image(s) or original stylized versions of that.
• Add supplier logo for: Corvana see images uploaded
Nice to have
• added tag lines or statements to re-enforce the focus of the luxury traveler that has earned that status of an elite flyer and traveler. We are open to any text or tag line ideas.
Should not have
• Clip-art of any kind.

```html
<!DOCTYPE html>
<html lang="en">
<head>
<meta charset="UTF-8">
<title>Velvet Horizon Voyages – Business Card</title>
<link rel="stylesheet" href="https://fonts.googleapis.com/css2?family=Cormorant+Garamond:ital,wght@0,600;1,500&family=Roboto:wght@400;500;700&display=swap">
<style>
  :root {
    --backdrop: #e9e4da;
    --card-green: #1d2d1b;
    --gold: #d8b65a;
    --gold-light: #f3df8c;
    --gold-deep: #b58d2e;
    --sky-blue: #3aaee6;
    --ink: #1f2a1c;
    --supplier-blue: #1b8fc2;
  }
  * { margin: 0; padding: 0; box-sizing: border-box; }
  html, body { width: 900px; height: 1200px; overflow: hidden; }
  body { background: var(--backdrop); position: relative; font-family: "Roboto", Arial, sans-serif; }

  .card {
    position: absolute;
    left: 90px;
    width: 722px;
    height: 420px;
    border-radius: 40px;
    background: var(--card-green);
    overflow: hidden;
  }
  .card--front { top: 135px; }
  .card--back { top: 632px; }

  /* brand name lockup */
  .brand {
    position: absolute;
    display: flex;
    align-items: center;
    gap: 18px;
    color: var(--gold);
    font-family: "Cormorant Garamond", Georgia, serif;
    font-weight: 600;
    line-height: 1.02;
  }
  .brand__dot {
    flex: none;
    border-radius: 50%;
    background: var(--gold);
  }
  .card--front .brand { left: 170px; top: 125px; font-size: 46px; }
  .card--front .brand__dot { width: 64px; height: 64px; }
  .card--back .brand { left: 350px; top: 55px; font-size: 38px; }
  .card--back .brand__dot { width: 54px; height: 54px; }

  .tagline {
    position: absolute;
    left: 0; right: 0; top: 345px;
    text-align: center;
    color: var(--gold);
    font-family: "Cormorant Garamond", Georgia, serif;
    font-style: italic;
    font-weight: 500;
    font-size: 30px;
  }
  .tagline__divider { display: inline-block; margin: 0 12px; }

  .swoosh { position: absolute; inset: 0; width: 100%; height: 100%; }

  .person { position: absolute; left: 44px; top: 32px; }
  .person__name { color: var(--sky-blue); font-weight: 700; font-size: 29px; }
  .person__role { color: var(--gold); font-size: 18px; margin-top: 4px; }

  .contact {
    position: absolute;
    display: flex;
    align-items: center;
    gap: 12px;
    color: var(--ink);
    font-size: 18px;
  }
  .contact--phone { left: 46px; top: 250px; }
  .contact--email { left: 46px; top: 283px; }
  .contact--web { left: 422px; top: 288px; }
  .contact--address {
    left: 46px; top: 355px;
    color: var(--gold-light);
    font-size: 16px;
    line-height: 1.55;
  }
  .contact__lines { border-left: 2px solid var(--gold); padding-left: 10px; }

  .icon {
    flex: none;
    width: 28px; height: 28px;
    border-radius: 50%;
    background: var(--card-green);
    border: 2px solid var(--gold);
    display: flex; align-items: center; justify-content: center;
  }
  .icon svg { width: 15px; height: 15px; }

  .supplier {
    position: absolute;
    left: 528px; top: 368px;
    color: var(--supplier-blue);
    font-family: "Roboto", Arial, sans-serif;
    font-weight: 700;
    font-size: 32px;
  }
</style>
</head>
<body>

<section class="card card--front">
  <div class="brand">
    <span class="brand__dot"></span>
    <span class="brand__name">Velvet Horizon<br>Voyages</span>
  </div>
  <p class="tagline">Travel smart<span class="tagline__divider">|</span>achieve more</p>
</section>

<section class="card card--back">
  <svg class="swoosh" viewBox="0 0 722 420" preserveAspectRatio="none" aria-hidden="true">
    <defs>
      <linearGradient id="goldSheen" x1="0" y1="0" x2="1" y2="0.3">
        <stop offset="0" stop-color="#b58d2e"/>
        <stop offset="0.35" stop-color="#f3df8c"/>
        <stop offset="0.65" stop-color="#d2ac48"/>
        <stop offset="1" stop-color="#f6e6a0"/>
      </linearGradient>
    </defs>
    <path d="M0,95 C200,140 450,200 722,232 L722,420 L520,420 C400,385 200,335 0,328 Z" fill="url(#goldSheen)"/>
    <path d="M0,160 C200,192 450,230 722,248 L722,258 C450,242 200,208 0,180 Z" fill="#1d2d1b"/>
    <path d="M0,316 C200,322 400,368 540,420 L520,420 C400,384 200,340 0,334 Z" fill="#1d2d1b" opacity="0.55"/>
    <path d="M0,334 C200,340 400,384 520,420 L0,420 Z" fill="#1d2d1b"/>
  </svg>

  <div class="person">
    <p class="person__name">Marcus Ellery</p>
    <p class="person__role">Managing director</p>
  </div>

  <div class="brand">
    <span class="brand__dot"></span>
    <span class="brand__name">Velvet Horizon<br>Voyages</span>
  </div>

  <p class="contact contact--phone">
    <span class="icon"><svg viewBox="0 0 16 16"><path d="M3 1h3l1 4-2 1c1 2 3 4 5 5l1-2 4 1v3c0 1-1 2-2 2C7 15 1 9 1 3c0-1 1-2 2-2z" fill="#d8b65a"/></svg></span>
    (403)271-4408
  </p>
  <p class="contact contact--email">
    <span class="icon"><svg viewBox="0 0 16 16"><rect x="1" y="3" width="14" height="10" fill="none" stroke="#d8b65a" stroke-width="1.6"/><path d="M1 3l7 6 7-6" fill="none" stroke="#d8b65a" stroke-width="1.6"/></svg></span>
    kdelane@velvethorizonvoyages.com
  </p>
  <p class="contact contact--web">
    <span class="icon"><svg viewBox="0 0 16 16"><circle cx="8" cy="8" r="6.5" fill="none" stroke="#d8b65a" stroke-width="1.5"/><path d="M1.5 8h13M8 1.5c-3 3.5-3 9.5 0 13M8 1.5c3 3.5 3 9.5 0 13" fill="none" stroke="#d8b65a" stroke-width="1.2"/></svg></span>
    www.velvethorizonvoyages.com
  </p>
  <div class="contact contact--address">
    <span class="icon"><svg viewBox="0 0 16 16"><path d="M8 1a5 5 0 0 1 5 5c0 4-5 9-5 9S3 10 3 6a5 5 0 0 1 5-5z" fill="none" stroke="#d8b65a" stroke-width="1.6"/><circle cx="8" cy="6" r="1.8" fill="#d8b65a"/></svg></span>
    <p class="contact__lines">212 Pinecrest Hollow Rd NW<br>Calgary, Alberta T2K 4W9 Canada</p>
  </div>

  <p class="supplier">Corvana</p>
</section>

</body>
</html>
```